KPT Building And Maintenance

Need a very professional looking double sided Buisiness card with all my details phone number, name, email, license number.

Target Market(s)

construction industry

Industry/Entity Type

building

Contact Information for Business Card

Name Dale Whitcombe. Email Address Info@KPTBuilding.example.au mobile number 0452918730 licence number 871406D. web site

```html
<!DOCTYPE html>
<html lang="en">
<head>
<meta charset="utf-8">
<title>KPT Building And Maintenance – Business Card</title>
<link href="https://fonts.googleapis.com/css2?family=Montserrat:wght@800&family=Open+Sans:wght@400;600&display=swap" rel="stylesheet">
<style>
  :root {
    --backdrop: #d3d3d3;
    --card-dark: #262626;
    --card-light: #ffffff;
    --brand-blue: #4a9bd8;
    --logo-grey: #333333;
    --text-light: #f2f2f2;
  }
  * { margin: 0; padding: 0; box-sizing: border-box; }
  html, body {
    width: 1200px;
    height: 788px;
    overflow: hidden;
    background: var(--backdrop);
  }
  .canvas {
    position: relative;
    width: 1200px;
    height: 788px;
  }
  .card {
    position: absolute;
    top: 239px;
    width: 540px;
    height: 310px;
    border-radius: 22px;
    overflow: hidden;
    box-shadow: 0 10px 24px rgba(0,0,0,0.25);
  }
  .card--front { left: 40px; background: var(--card-light); }
  .card--back  { left: 620px; background: var(--card-dark); }

  .front-shapes { position: absolute; inset: 0; }

  .wordmark {
    font-family: "Montserrat", sans-serif;
    font-weight: 800;
    letter-spacing: 1px;
    text-transform: uppercase;
    line-height: 1;
  }
  .wordmark--front {
    position: absolute;
    left: 36px;
    top: 42px;
    font-size: 42px;
    color: var(--logo-grey);
  }
  .wordmark--back {
    position: absolute;
    inset: 0;
    display: flex;
    flex-direction: column;
    align-items: center;
    justify-content: center;
    color: var(--card-light);
  }
  .wordmark--back .wordmark-main { font-size: 78px; letter-spacing: 3px; }
  .wordmark--back .wordmark-sub { font-size: 34px; letter-spacing: 4px; margin-top: 6px; }

  .person {
    position: absolute;
    right: 215px;
    top: 222px;
    text-align: right;
    font-family: "Open Sans", sans-serif;
    color: var(--text-light);
  }
  .person-name {
    font-family: "Open Sans", sans-serif;
    font-weight: 600;
    font-size: 16px;
    color: var(--brand-blue);
    letter-spacing: 0.5px;
    text-transform: uppercase;
  }
  .person-role, .person-licence { font-size: 11.5px; line-height: 1.45; }

  .divider {
    position: absolute;
    left: 338px;
    top: 218px;
    width: 1.5px;
    height: 62px;
    background: var(--brand-blue);
  }

  .contacts {
    position: absolute;
    left: 352px;
    top: 210px;
    list-style: none;
    font-family: "Open Sans", sans-serif;
    font-size: 11.5px;
    color: var(--text-light);
  }
  .contact-item {
    display: flex;
    align-items: center;
    gap: 6px;
    line-height: 1;
    margin-bottom: 9px;
  }
  .contact-icon { width: 10px; height: 10px; flex: none; }
</style>
</head>
<body>
<main class="canvas">

  <section class="card card--front" aria-label="Business card front">
    <svg class="front-shapes" width="540" height="310" viewBox="0 0 540 310" aria-hidden="true">
      <polygon points="90,310 240,140 540,78 540,310" fill="var(--card-dark)"/>
      <polyline points="70,310 233,126 540,64" fill="none" stroke="var(--brand-blue)" stroke-width="3"/>
    </svg>

    <h1 class="wordmark wordmark--front">KPT Building</h1>

    <div class="person">
      <p class="person-name">Dale Whitcombe</p>
      <p class="person-role">Managing Director</p>
      <p class="person-licence">Licence Number 871406D</p>
    </div>

    <div class="divider"></div>

    <ul class="contacts">
      <li class="contact-item">
        <svg class="contact-icon" viewBox="0 0 10 10" aria-hidden="true"><path d="M2 1 L4 1 L4.6 3 L3.5 4 Q4.5 6 6 6.5 L7 5.4 L9 6 L9 8 Q9 9 8 9 Q1 8.5 1 2 Q1 1 2 1 Z" fill="var(--brand-blue)"/></svg>
        <span>0452918730</span>
      </li>
      <li class="contact-item">
        <svg class="contact-icon" viewBox="0 0 10 10" aria-hidden="true"><rect x="0.5" y="2" width="9" height="6" fill="var(--brand-blue)"/><polyline points="0.5,2 5,5.5 9.5,2" fill="none" stroke="var(--card-dark)" stroke-width="1"/></svg>
        <span>Info@KPTBuilding.example.au</span>
      </li>
      <li class="contact-item">
        <svg class="contact-icon" viewBox="0 0 10 10" aria-hidden="true"><circle cx="5" cy="5" r="4.5" fill="var(--brand-blue)"/><path d="M0.5 5 H9.5 M5 0.5 Q2.5 5 5 9.5 M5 0.5 Q7.5 5 5 9.5" fill="none" stroke="var(--card-dark)" stroke-width="0.7"/></svg>
        <span>www.KPTBuilding.example.au</span>
      </li>
    </ul>
  </section>

  <section class="card card--back" aria-label="Business card back">
    <div class="wordmark wordmark--back">
      <span class="wordmark-main">KPT</span>
      <span class="wordmark-sub">Building</span>
    </div>
  </section>

</main>
</body>
</html>
```